Stellenanzeigen zur Mitarbeitergewinnung über soziale Medien & Google / YouTube
Zielgruppe
Wir sind zwei Brüder und Inhaber der Zahnarztpraxis „ Zahnmedizin am Lindenhof“ in Bochum.
Wir benötigen zur Mitarbeitergewinnung ein neues, modernes Konzept. Insbesondere stehen Stellenanzeigen im Vordergrund, die in sozialen Medien, wie Instagram, aber auch über Google und YouTube angezeigt werden sollen und potentielle Mitarbeiter auf unsere eigene Landingpage zur Mitarbeitergewinnung führen
Es geht nicht darum, Patienten anzusprechen, sondern ausschließlich um Mitarbeitergewinnung.
Aufgabenstellung
Wir haben Interesse an einem Gesamtkonzept, eine Serie von Anzeigen, die unsere Praxis widerspiegeln, uns als Inhaber zeigen, sowie unsere vorhandenen Mitarbeiterinnen einbinden.
Aufgrund der Vielzahl von Stellenanzeigen im medizinischen Bereich, braucht es neue Ideen. Wir möchten uns deutlich von den vorhandenen, unzähligen Anzeigen bei Instagram abheben. Hier sind kreative Ideen erwünscht.
Wir haben eine zur Mitarbeitergewinnung vorhandene Homepage, die Videos und Aussagekräftige Fotos und Texte beinhaltet. Dort gibt es die Möglichkeit, sich direkt auf eine freie Stelle unkompliziert zu bewerben.
Wir möchten über die neuen Anzeigen potentielle Mitarbeiter dazu bewegen, sich diese Homepage anzusehen und sich gegebenfalls direkt zu bewerben.
Wir freuen uns über ein Gesamtkonzept, gerne verschiedene Stellenanzeigen, die aber ineinander schlüssig sind. Beispielsweise mit anderen Überschriften oder mit verschiedenen Fotos, die wir bereitstellen. Die vorgeschlagenen Fotos können gerne benutzt werden, alternativ sind wir im Hinblick auf das Gesamtkonzept auch offen für andere Ideen und Fotos. Da die Mitbewerbersituation extrem hoch ist, macht es Sinn, sich vorhandene Stellenanzeigen anzusehen, damit wir deutlich die Vorteile unserer Praxis transportieren und uns klar positionieren.
Wir Inhaber, Brüder, Dr. Tobias und Lars Wendrich, sind Ende 30, Ruhrpottkinder, haben eine moderne Praxis zentral in Bochum am Eichgarten.
Unsere Praxis ist im modernen und ansprechenden Lindenhof. Wir haben bereits ein großes Team und zwei weitere angestellte Zahnärztinnen. Bei uns gibt es eine faire Bezahlung, Zusatzleistungen, die eine Gutscheinkarte oder die Möglichkeit eines Stellplatzes oder ÖPNV Ticket. Wir machen keine Überstunden, sind freundliche und entspannte Chefs. Wir legen Wert auf Qualität und nehmen uns für uns Zeit für Patienten und Mitarbeiter.
Ziel sollte es sein, motivierte und leistungsstarke Mita..

```html
<!DOCTYPE html>
<html lang="de">
<head>
<meta charset="utf-8">
<title>Stellenanzeigen Zahnmedizinische Fachangestellte</title>
<link rel="stylesheet" href="https://fonts.googleapis.com/css2?family=Archivo:wght@400;500;600;700;800&display=swap">
<style>
  :root {
    --page: #ffffff;
    --slate: #4b535b;
    --sand: #d2c9a2;
    --steel: #aab3c3;
    --panel: #a3abbb;
    --button: #a9afbc;
    --ink: #3f464d;
    --white: #ffffff;
    --brick: #7a4a38;
    --brick-dark: #5b372b;
    --sky: #c9dcea;
  }
  * { box-sizing: border-box; margin: 0; padding: 0; }
  html, body {
    width: 1200px; height: 725px; overflow: hidden;
    background: var(--page);
    font-family: "Archivo", "Helvetica Neue", Arial, sans-serif;
  }
  .stage { position: relative; width: 1200px; height: 725px; }
  .ad {
    position: absolute; top: 145px;
    width: 433px; height: 432px;
    background: var(--slate);
    overflow: hidden;
    box-shadow: 0 10px 30px rgba(0,0,0,.08);
  }
  .ad--training { left: 145px; }
  .ad--hiring { left: 620px; }
  .ad__header { position: absolute; left: 42px; top: 28px; }
  .ad__kicker {
    color: var(--sand); font-weight: 700; font-size: 25px; letter-spacing: -.2px;
    line-height: 1;
  }
  .ad__title {
    margin-top: 6px;
    color: var(--steel); font-weight: 800; font-size: 26.5px; line-height: .98;
    letter-spacing: .2px; text-transform: uppercase;
  }
  .ad__place {
    margin-top: 6px; color: var(--white); font-size: 9.5px; font-weight: 500;
    letter-spacing: .3px;
  }
  .ad__photo {
    position: absolute; top: 149px;
    background:
      linear-gradient(90deg, transparent 0 78%, var(--sky) 78%),
      linear-gradient(180deg, var(--brick) 0%, var(--brick-dark) 100%);
  }
  .ad--training .ad__photo { left: 133px; width: 300px; height: 283px; }
  .ad--hiring .ad__photo {
    left: 0; width: 298px; height: 283px;
    background:
      linear-gradient(90deg, var(--sky) 0 12%, transparent 12%),
      linear-gradient(180deg, var(--brick) 0%, var(--brick-dark) 100%);
  }
  .benefits {
    position: absolute; top: 176px;
    background: var(--panel);
    list-style: none;
    padding: 12px 14px;
  }
  .ad--training .benefits { left: 42px; width: 223px; height: 159px; }
  .ad--hiring .benefits { left: 215px; width: 174px; height: 159px; }
  .benefits li {
    display: flex; align-items: center; gap: 9px;
    color: var(--white); font-size: 14.5px; font-weight: 500;
    height: 27px; white-space: nowrap;
  }
  .benefits svg { flex: none; }
  .apply {
    position: absolute; top: 360px; height: 31px;
    background: var(--button); color: var(--ink);
    font-weight: 700; white-space: nowrap;
    display: flex; align-items: center; justify-content: center;
    padding: 0 6px;
  }
  .ad--training .apply { left: 42px; width: 96px; font-size: 10.5px; }
  .ad--hiring .apply { left: 215px; width: 142px; font-size: 12px; }
</style>
</head>
<body>
<div class="stage">

  <section class="ad ad--training">
    <div class="ad__header">
      <p class="ad__kicker">Ausbildung</p>
      <h2 class="ad__title">Zahnmedizinische<br>Fachangestellte</h2>
      <p class="ad__place">IN BOCHUNM</p>
    </div>
    <div class="ad__photo" role="img" aria-label="Foto des modernen Praxisgebäudes aus rotem Backstein vor blauem Himmel"></div>
    <ul class="benefits">
      <li><svg width="14" height="11" viewBox="0 0 14 11"><path d="M1 5.5l4 4L13 1" fill="none" stroke="#fff" stroke-width="1.8"/></svg>Work-Life-Balance</li>
      <li><svg width="14" height="11" viewBox="0 0 14 11"><path d="M1 5.5l4 4L13 1" fill="none" stroke="#fff" stroke-width="1.8"/></svg>Weiterbildung</li>
      <li><svg width="14" height="11" viewBox="0 0 14 11"><path d="M1 5.5l4 4L13 1" fill="none" stroke="#fff" stroke-width="1.8"/></svg>Zentrale Lage</li>
      <li><svg width="14" height="11" viewBox="0 0 14 11"><path d="M1 5.5l4 4L13 1" fill="none" stroke="#fff" stroke-width="1.8"/></svg>Guter Erreichbarkeit</li>
      <li><svg width="14" height="11" viewBox="0 0 14 11"><path d="M1 5.5l4 4L13 1" fill="none" stroke="#fff" stroke-width="1.8"/></svg>Moderne Praxis</li>
    </ul>
    <div class="apply">Jetzt bewerben!</div>
  </section>

  <section class="ad ad--hiring">
    <div class="ad__header">
      <p class="ad__kicker">Wir suchen:</p>
      <h2 class="ad__title">Zahnmedizinische<br>Fachangestellte</h2>
      <p class="ad__place">IN BOCHUNM</p>
    </div>
    <div class="ad__photo" role="img" aria-label="Foto des modernen Praxisgebäudes aus rotem Backstein vor blauem Himmel"></div>
    <ul class="benefits">
      <li><svg width="14" height="11" viewBox="0 0 14 11"><path d="M1 5.5l4 4L13 1" fill="none" stroke="#fff" stroke-width="1.8"/></svg>Work-Life-Balance</li>
      <li><svg width="14" height="11" viewBox="0 0 14 11"><path d="M1 5.5l4 4L13 1" fill="none" stroke="#fff" stroke-width="1.8"/></svg>Weiterbildung</li>
      <li><svg width="14" height="11" viewBox="0 0 14 11"><path d="M1 5.5l4 4L13 1" fill="none" stroke="#fff" stroke-width="1.8"/></svg>Zentrale Lage</li>
      <li><svg width="14" height="11" viewBox="0 0 14 11"><path d="M1 5.5l4 4L13 1" fill="none" stroke="#fff" stroke-width="1.8"/></svg>Guter Erreichbarkeit</li>
      <li><svg width="14" height="11" viewBox="0 0 14 11"><path d="M1 5.5l4 4L13 1" fill="none" stroke="#fff" stroke-width="1.8"/></svg>Moderne Praxis</li>
    </ul>
    <div class="apply">Jetzt bewerben!</div>
  </section>

</div>
</body>
</html>
```